Maple Bug Guard Business Cards

A modern business card with a predominantly white background and a sleek design featuring Maple with complimentary greys or blacks to convey a professional and contemporary look.

Front:
Primarily white background. Limited use of company purple color can be neighbored by greys.
Text: Name, Title, Cell Phone, Office Phone, Website, email address

Back:
Background Continuation: The back of the card maintains the white background for consistency.
Company name “Maple” in company color and font, “Bug Guard” underneath or underneath left justified of “Maple.”
A subtle pattern or texture in shades of grey to add depth behind the company Logo in font.

logo color: hex #6212ab
font: antique olive nord D Regular

```html
<!DOCTYPE html>
<html lang="en">
<head>
<meta charset="utf-8">
<title>Maple Bug Guard Business Cards</title>
<link rel="stylesheet" href="https://fonts.googleapis.com/css2?family=Roboto:wght@400;700;900&display=swap">
<style>
  :root {
    --stage: #3c3c3c;
    --card: #ffffff;
    --brand: #6212ab;
    --ink: #4a4a4a;
    --muted: #8a8a8a;
    --rule: #d6d6d6;
    --band-grey: #555555;
    --texture-light: #f4f4f4;
    --texture-dark: #e2e2e2;
  }
  * { box-sizing: border-box; margin: 0; padding: 0; }
  html, body { width: 1200px; height: 803px; overflow: hidden; }
  body {
    background: var(--stage);
    font-family: "Roboto", Arial, sans-serif;
    position: relative;
  }
  .card {
    position: absolute;
    top: 253px;
    width: 520px;
    height: 297px;
    background: var(--card);
    border-radius: 22px;
    overflow: hidden;
    box-shadow: 0 18px 40px rgba(0,0,0,.45);
  }
  .card--front { left: 50px; }
  .card--back { left: 630px; }

  .wordmark {
    font-weight: 900;
    color: var(--brand);
    text-transform: uppercase;
    line-height: 1;
    letter-spacing: 1px;
    white-space: nowrap;
  }
  .wordmark span { display: block; }
  .card--front .wordmark {
    position: absolute;
    top: 34px;
    left: 190px;
    font-size: 38px;
  }
  .card--back .texture {
    position: absolute;
    inset: 0;
    background: radial-gradient(ellipse at 50% 50%, var(--texture-light) 0%, var(--texture-dark) 100%);
    opacity: .6;
  }
  .card--back .wordmark {
    position: absolute;
    top: 50%;
    left: 50%;
    transform: translate(-50%, -50%);
    font-size: 52px;
  }

  .divider {
    position: absolute;
    left: 40px;
    right: 40px;
    top: 188px;
    height: 1px;
    background: var(--rule);
  }
  .person { position: absolute; left: 40px; top: 142px; }
  .person__name { font-size: 22px; font-weight: 700; color: var(--brand); }
  .person__title { font-size: 12px; color: var(--muted); margin-top: 2px; }

  .contacts {
    position: absolute;
    left: 40px;
    top: 198px;
    list-style: none;
    font-size: 13px;
    color: var(--ink);
  }
  .contacts li { display: flex; align-items: center; gap: 9px; height: 19px; }
  .contacts svg { width: 12px; height: 12px; fill: var(--brand); }

  .address {
    position: absolute;
    right: 40px;
    top: 148px;
    text-align: right;
    font-size: 13px;
    color: var(--ink);
    line-height: 1.35;
  }
  .band { position: absolute; left: 0; bottom: 0; width: 520px; height: 40px; }
  .website {
    position: absolute;
    right: 36px;
    bottom: 8px;
    font-size: 13px;
    color: #fff;
  }
</style>
</head>
<body>

<section class="card card--front" aria-label="Business card front">
  <div class="wordmark"><span>Maple</span><span>Bug Guard</span></div>

  <div class="person">
    <p class="person__name">Daniel Hart</p>
    <p class="person__title">President</p>
  </div>

  <div class="address">
    <p>4120 Willow Crest Road</p>
    <p>Riverton, Canada 58213</p>
  </div>

  <div class="divider"></div>

  <ul class="contacts">
    <li>
      <svg viewBox="0 0 12 12" aria-hidden="true"><path d="M3 1l2 2.5-1.2 1.3a7 7 0 0 0 3.4 3.4L8.5 7 11 9l-1.3 2C5.5 11 1 6.5 1 2.3z"/></svg>
      555-210-4831
    </li>
    <li>
      <svg viewBox="0 0 12 12" aria-hidden="true"><path d="M3 0h6a1 1 0 0 1 1 1v10a1 1 0 0 1-1 1H3a1 1 0 0 1-1-1V1a1 1 0 0 1 1-1zm.5 1.5v8h5v-8z"/></svg>
      555-318-7720
    </li>
    <li>
      <svg viewBox="0 0 12 12" aria-hidden="true"><path d="M0 2h12v8H0zM1 3v.3l5 3.4 5-3.4V3z"/></svg>
      info@maplebugguard.com
    </li>
  </ul>

  <svg class="band" viewBox="0 0 520 40" aria-hidden="true">
    <path d="M0 23 H296 L304 15 H520 V40 H0 Z" fill="var(--band-grey)"/>
    <path d="M0 31 H300 L312 10 H520 V40 H0 Z" fill="var(--brand)"/>
  </svg>
  <p class="website">www.maplebugguard.com</p>
</section>

<section class="card card--back" aria-label="Business card back">
  <div class="texture" role="img" aria-label="Subtle grey texture behind the company name"></div>
  <div class="wordmark"><span>Maple</span><span>Bug Guard</span></div>
</section>

</body>
</html>
```